We need a flyer (size Din A4, folded, see image).
Attached you will find the content with a rough arrangement.
The inner part will contain some Q&A, we have sketched two possible arrangements of the content.
We are looking for a professional design and a good, clean layout.
Maybe you have some ideas how to arrange the content in a smarter way, we are open for suggestions.
The draft contains no images. It would be good to have an explaining image at least on the front of the flyer.
Attached you will find some stock photos we are using on our website, but you can also propose your own images.
If useful, here is our webpage:
https://vorn-strom.de/
and the landing page for the offering
https://vorn-strom. en/charging-solutions-for-house-management-and-routes/
(this landing page is not professionally designed, so feel free to create a better design for the flyer)
Our target group are real estate managers/facility managers of larger apartment buildings.
The offering is: full-serviced solutions for charging infrastructure for electric cars at the parking lots for residents.
Please do not hesitate to contact me, if you need further information.
Target Market(s)
Professionals in real estate management, facility management
Industry/Entity Type
charging infrastructures for electric cars, focus: appartment buildings

```html
<!DOCTYPE html>
<html lang="de">
<head>
<meta charset="utf-8">
<title>vorn-strom Faltflyer</title>
<link href="https://fonts.googleapis.com/css2?family=Poppins:wght@400;500;600;700;800&display=swap" rel="stylesheet">
<style>
:root{
  --bg:#e6e8ec;
  --navy:#1b1f3d;
  --navy-2:#232849;
  --navy-card:#2c3256;
  --white:#ffffff;
  --paper:#eceef2;
  --ink:#1b1f3d;
  --purple:#8a3ddb;
  --violet:#a24ee6;
  --magenta:#e0249a;
  --muted:#b9bdd3;
}
*{box-sizing:border-box;margin:0;padding:0}
html,body{width:1200px;height:1200px;overflow:hidden}
body{background:var(--bg);font-family:"Poppins",sans-serif;color:var(--ink);position:relative}
.spread{position:absolute;left:204px;width:792px;height:560px;display:flex;box-shadow:0 10px 30px rgba(20,25,50,.18)}
.spread--outside{top:26px}
.spread--inside{top:614px}
.panel{width:264px;height:100%;position:relative;overflow:hidden}
.panel + .panel{border-left:1px solid rgba(0,0,0,.08)}

/* outside: back panel */
.back-top{background:var(--navy);color:var(--white);height:280px;padding:38px 26px}
.back-top h2{font-size:16px;font-weight:600;line-height:1.45}
.ticks{list-style:none;margin-top:10px}
.ticks li{font-size:16px;font-weight:600;line-height:1.45;display:flex;align-items:center;gap:8px}
.ticks svg{width:13px;height:13px;flex:none}
.back-bottom{background:var(--paper);height:280px;padding:30px 26px}
.back-bottom p{font-size:10.5px;font-weight:600;line-height:1.45;margin-bottom:16px}
.back-bottom .accent{color:var(--purple)}

/* outside: contact panel */
.contact{background:var(--navy-2);color:var(--white);padding:150px 30px 0}
.contact h3{font-size:14px;font-weight:600;line-height:1.4}
.contact .url{color:var(--violet);font-size:13px;font-weight:600;margin-top:22px}
.contact .or{font-size:13px;font-weight:600;margin-top:16px}
.contact .phone{color:var(--magenta);font-size:13px;font-weight:700;margin-top:16px}

/* outside: front panel */
.front{background:var(--white)}
.front-strip{height:44px;background:linear-gradient(90deg,#6a34c9,#c232b6);color:var(--white);font-size:7px;line-height:1.4;padding:9px 14px;text-align:right}
.front-photo{height:150px;background:radial-gradient(circle at 72% 55%,#3a8cff 0,#5a6fd6 18%,#b9c3e6 45%,#7d82b0 75%,#3b3f68 100%)}
.front-title{height:230px;background:linear-gradient(160deg,#7a3ad8 0%,#a13bd0 45%,#e0249a 100%);color:var(--white);padding:16px 18px}
.brand{display:flex;align-items:center;gap:6px;font-size:10px;font-weight:600}
.brand i{width:9px;height:9px;border-radius:50%;background:var(--white);display:block}
.front-title h1{font-size:30px;font-weight:800;line-height:1;margin-top:10px}
.front-title .sub{font-size:14px;font-weight:700;line-height:1.2;margin-top:4px}
.front-title .claim{font-size:17px;font-weight:700;line-height:1.15;margin-top:14px}
.front-foot{padding:16px 18px;font-size:7.5px;line-height:1.5;font-weight:500;color:var(--ink)}
.front-foot p + p{margin-top:8px}

/* inside: questions */
.questions{background:var(--paper);padding:30px 22px}
.questions h2{color:var(--purple);font-size:14px;font-weight:700;margin-bottom:14px}
.question{display:flex;justify-content:space-between;align-items:flex-end;gap:8px;margin-bottom:14px}
.question p{font-size:10.5px;font-weight:700;line-height:1.35}
.question svg{width:18px;height:12px;flex:none;margin-bottom:2px}

/* inside: solutions */
.solutions{background:var(--navy-2);color:var(--muted);padding:26px 16px}
.solutions h2{color:var(--violet);font-size:11px;font-weight:700;margin-bottom:10px}
.answer{background:var(--navy-card);padding:8px 10px;font-size:7.5px;line-height:1.5;margin-bottom:8px}
.answer:nth-child(odd){background:#262c4f}

/* inside: steps */
.steps{background:var(--navy);color:var(--white);padding:30px 26px}
.steps h2{color:var(--magenta);font-size:11px;font-weight:700;line-height:1.4;margin-bottom:26px}
.step{margin-bottom:24px}
.step h3{font-size:16px;font-weight:700}
.step p{font-size:9.5px;line-height:1.45;color:var(--muted);margin-top:3px}
</style>
</head>
<body>

<section class="spread spread--outside">
  <div class="panel back">
    <div class="back-top">
      <h2>Bieten Sie Ihren Bewohnern Lademöglichkeiten für ihre Elektrofahrzeuge –</h2>
      <ul class="ticks">
        <li><svg viewBox="0 0 14 14"><path d="M2 7.5l3.2 3.2L12 3.5" fill="none" stroke="#fff" stroke-width="2"/></svg>einfach,</li>
        <li><svg viewBox="0 0 14 14"><path d="M2 7.5l3.2 3.2L12 3.5" fill="none" stroke="#fff" stroke-width="2"/></svg>unkompliziert und</li>
        <li><svg viewBox="0 0 14 14"><path d="M2 7.5l3.2 3.2L12 3.5" fill="none" stroke="#fff" stroke-width="2"/></svg>zukunftsfähig.</li>
      </ul>
    </div>
    <div class="back-bottom">
      <p>Zukunftsfähig durch flexibles Abrechnungsmodell für verschiedene Einsatzmöglichkeiten.</p>
      <p class="accent">Leichter, schneller Einstieg in das Thema, unkompliziert und professionelle Abwicklung</p>
      <p>Aufbau und Betrieb von Ladelösungen speziell für Hausverwaltungen und WEGs</p>
    </div>
  </div>

  <div class="panel contact">
    <h3>Jetzt Beratungsgespräch anfordern unter:</h3>
    <p class="url">https://vorn-strom.de/WEG</p>
    <p class="or">oder</p>
    <p class="phone">0800 / 555 01 23</p>
  </div>

  <div class="panel front">
    <div class="front-strip">Ladelösungen für Hausverwaltungen und WEGs – von der ersten Prüfung bis zum laufenden Betrieb.</div>
    <div class="front-photo" role="img" aria-label="Foto: Ladestecker an einem Elektroauto mit blau leuchtendem Ladeanschluss"></div>
    <div class="front-title">
      <div class="brand"><i></i>vorn-strom.de</div>
      <h1>Flexible</h1>
      <p class="sub">Ladeinfrastrukturen für die Elektromobilität</p>
      <p class="claim">für Mieter und Eigentümer einfach, unkompliziert und zukunftsfähig</p>
    </div>
    <div class="front-foot">
      <p>Hausverwaltungen stehen vor dem Wunsch von Mietern und Eigentümern nach einer eigenen Lademöglichkeit.</p>
      <p>vorn-strom plant, installiert und betreibt die passende Ladeinfrastruktur für Ihr Objekt.</p>
    </div>
  </div>
</section>

<section class="spread spread--inside">
  <div class="panel questions">
    <h2>Problem / Fragestellung</h2>
    <div class="question"><p>Ein Bewohner will eine Wallbox – was tun?</p><svg viewBox="0 0 18 12"><path d="M0 6h14M10 1l6 5-6 5" fill="none" stroke="#1b1f3d" stroke-width="2.2"/></svg></div>
    <div class="question"><p>Der Stromanschluss reicht nicht, wenn alle Bewohner eine Wallbox wollen!</p><svg viewBox="0 0 18 12"><path d="M0 6h14M10 1l6 5-6 5" fill="none" stroke="#1b1f3d" stroke-width="2.2"/></svg></div>
    <div class="question"><p>Sind die Vorabprüfung und der Einbau einer Ladeinfrastruktur teuer? Wie überzeugt man die WEG von den Kosten?</p><svg viewBox="0 0 18 12"><path d="M0 6h14M10 1l6 5-6 5" fill="none" stroke="#1b1f3d" stroke-width="2.2"/></svg></div>
    <div class="question"><p>Die Bewohner haben keine fest zugeordneten Stellplätze</p><svg viewBox="0 0 18 12"><path d="M0 6h14M10 1l6 5-6 5" fill="none" stroke="#1b1f3d" stroke-width="2.2"/></svg></div>
    <div class="question"><p>Wer kann helfen, eine professionelle und zukunftsfähige Ladeinfrastruktur zu entwickeln?</p><svg viewBox="0 0 18 12"><path d="M0 6h14M10 1l6 5-6 5" fill="none" stroke="#1b1f3d" stroke-width="2.2"/></svg></div>
    <div class="question"><p>Bei uns wurden bereits Wallboxen von einzelnen Mietern installiert, was nun?</p><svg viewBox="0 0 18 12"><path d="M0 6h14M10 1l6 5-6 5" fill="none" stroke="#1b1f3d" stroke-width="2.2"/></svg></div>
  </div>

  <div class="panel solutions">
    <h2>Der Lösungsansatz von vorn-strom</h2>
    <div class="answer">Ein Bewohner hat nach einer Wallbox gefragt? Wir prüfen, ob sich das Objekt für eine gemeinsame Lösung eignet, und schlagen die nächsten Schritte vor.</div>
    <div class="answer">Mit Hilfe des Last-Managements von vorn-strom lässt sich die verfügbare Strom-Kapazität intelligent steuern, so dass der Hausanschluss in der Regel langfristig ausreicht.</div>
    <div class="answer">Bei der Lösung von vorn-strom werden nur die aktuell benötigten Komponenten installiert – die Anlage wächst schrittweise mit der Nachfrage.</div>
    <div class="answer">Mit dem optionalen Mietmodell entstehen der WEG keine oder nur geringe Kosten; die Ladevorgänge werden verbrauchsgenau abgerechnet.</div>
    <div class="answer">Der Anschluss an den Wohnungszähler ist nicht notwendig. vorn-strom rechnet auf Wunsch mit jedem Nutzer direkt ab.</div>
    <div class="answer">Neben der Umsetzung unterstützt vorn-strom die Hausverwaltung bei der Abstimmung mit der Eigentümerversammlung.</div>
    <div class="answer">In vielen Fällen kann Hardware anderer Hersteller in die Abrechnungslösung von vorn-strom integriert werden.</div>
  </div>

  <div class="panel steps">
    <h2>Die Schritte zur Ladeinfrastruktur in Ihrem Objekt:</h2>
    <div class="step"><h3>1. Erstprüfung</h3><p>Machbarkeitsprüfung<br>Abschätzung, Planung<br>nächster Schritte</p></div>
    <div class="step"><h3>2. Konzeption</h3><p>Planung der Anlage<br>Abstimmung Netzbetreiber<br>Kostenkalkulation</p></div>
    <div class="step"><h3>3. Installation</h3><p>Installation von Verkabelung<br>und Elektrotechnik<br>Installation der Wallboxen<br>Setup der Abrechnungssysteme</p></div>
    <div class="step"><h3>4. Betrieb</h3><p>Technischer Betrieb<br>Abrechnung<br>Regelmäßige Wartung (DGUV3)<br>Anmeldung und Verwaltung neuer Nutzer</p></div>
  </div>
</section>

</body>
</html>
```